Biz cards

Need some business cards to handout when finding clients for medical marijuana

Industry/Entity Type

Business

Contact Information for Business Card

Name: Dev Tolland
Cell #604-555-0193
Instagram: lunarvalleyfarmsbc

Requirements
Must have
• Needs to say ( on back of card with my info )
• MMAR Producer
• Marijuana Enthusiest and connoisseur

```html
<!DOCTYPE html>
<html lang="en">
<head>
<meta charset="utf-8">
<title>Lunar Valley – Business Cards</title>
<link rel="stylesheet" href="https://fonts.googleapis.com/css2?family=Exo+2:wght@400;600;800&display=swap">
<style>
  :root {
    --stage: #e9e7e3;
    --card: #f4f4f4;
    --ink: #111111;
    --red: #d8242b;
    --leaf-dark: #1a2416;
    --leaf-mid: #4e7a3a;
    --leaf-light: #a9b8a0;
  }
  * { box-sizing: border-box; margin: 0; padding: 0; }
  html, body {
    width: 1200px; height: 780px; overflow: hidden;
    background: var(--stage);
    font-family: "Exo 2", sans-serif;
  }
  .canvas { position: relative; width: 1200px; height: 780px; }

  .card {
    position: absolute;
    border-radius: 18px;
    overflow: hidden;
    box-shadow: 0 10px 28px rgba(0,0,0,.18);
  }

  /* Front */
  .card-front {
    left: 70px; top: 218px; width: 600px; height: 344px;
    background: var(--card);
  }
  .front-band {
    position: absolute; background: var(--red);
    height: 34px; width: 150px;
  }
  .front-band--top { top: 0; right: 0; }
  .front-band--bottom { bottom: 0; left: 0; }

  .front-content {
    position: absolute; left: 70px; top: 78px; right: 40px;
    display: flex; flex-direction: column; gap: 0;
  }
  .brand {
    display: flex; align-items: center; gap: 14px;
    margin-bottom: 26px;
  }
  .brand-square { width: 26px; height: 26px; background: var(--red); }
  .brand-name {
    font-weight: 800; font-size: 44px; letter-spacing: 1px;
    color: var(--ink); text-transform: uppercase; line-height: 1;
  }
  .contact { padding-left: 40px; }
  .contact-name {
    font-weight: 800; font-size: 26px; color: var(--ink);
    text-transform: uppercase; line-height: 1.1;
  }
  .contact-role {
    font-weight: 400; font-size: 17px; color: var(--red);
    margin-bottom: 14px;
  }
  .contact-line { font-size: 18px; color: var(--ink); line-height: 1.45; }
  .contact-label { color: var(--red); }

  /* Back */
  .card-back {
    left: 780px; top: 90px; width: 344px; height: 600px;
    background: var(--red);
  }
  .back-photo {
    position: absolute; left: 0; top: 0; width: 100%; height: 470px;
    background:
      radial-gradient(ellipse at 45% 30%, var(--leaf-light) 0%, rgba(169,184,160,0) 35%),
      radial-gradient(ellipse at 60% 70%, var(--leaf-mid) 0%, rgba(78,122,58,0) 60%),
      var(--leaf-dark);
  }
  .back-rule {
    position: absolute; left: 0; top: 470px; width: 100%; height: 8px;
    background: var(--card);
  }
  .back-tagline {
    position: absolute; left: 0; right: 0; top: 478px; bottom: 0;
    display: flex; align-items: center; justify-content: center;
    text-align: center;
    font-weight: 600; font-size: 22px; line-height: 1.2; color: var(--ink);
  }
</style>
</head>
<body>
<main class="canvas">

  <section class="card card-front" aria-label="Business card front">
    <div class="front-band front-band--top"></div>
    <div class="front-band front-band--bottom"></div>

    <div class="front-content">
      <div class="brand">
        <span class="brand-square"></span>
        <span class="brand-name">Lunar Valley</span>
      </div>
      <div class="contact">
        <p class="contact-name">Dev Tolland</p>
        <p class="contact-role">MMAR Producer</p>
        <p class="contact-line"><span class="contact-label">Cell:</span> 604-555-0193</p>
        <p class="contact-line"><span class="contact-label">Instagram:</span> lunarvalleyfarmsbc</p>
      </div>
    </div>
  </section>

  <section class="card card-back" aria-label="Business card back">
    <div class="back-photo" role="img" aria-label="Close-up photograph of a flowering cannabis bud with green leaves on a dark background"></div>
    <div class="back-rule"></div>
    <p class="back-tagline">Marijuana Enthusiest<br>and connoisseur</p>
  </section>

</main>
</body>
</html>
```